Plakat für Hersteller von Maultaschen und Knödeln
Zielgruppe
Mit meiner Manufaktur Rinnfalten & Co stelle ich Maultaschen und Knödel her. Produziert wird mit hochwertigen, möglichst regionalen Zutaten und mit dem Anspruch, traditionelle Klassiker in zeitgemäßer Qualität anzubieten.
Im Mittelpunkt stehen Frische, Transparenz und ehrliches Handwerk. Die Produkte werden mit Sorgfalt hergestellt und sind für den direkten Verkauf auf dem Brunnwaldener Wochenmarkt bestimmt. Rinnfalten & Co verbindet bodenständige Küche mit regionaler Identität – unkompliziert, authentisch und genussorientiert.
Zielgruppe rund um den Brunnwaldener Wochenmarkt:
- Marktbesucher mit Qualitätsbewusstsein, die gezielt regionale und handwerklich hergestellte Lebensmittel kaufen
- Berufstätige und Familien, die hochwertige, frisch produzierte Gerichte für zu Hause suchen
- Genussorientierte Kundinnen und Kunden, die traditionelle Küche schätzen
- Seniorinnen und Senioren, die klassische Hausmannskost bevorzugen
- Regionalverbundenen Verbraucherinnen und Verbrauchern, die lokale Anbieter unterstützen möchten
Der Brunnwaldener Wochenmarkt zieht ein vielfältiges Publikum an, das Wert auf persönliche Beratung, Frische und nachvollziehbare Herkunft legt. Rinnfalten positioniert sich hier als authentischer, spezialisierter Anbieter für handgemachte Teigklassiker mit klarem kulinarischem Profil.
Aufgabenstellung
Das Plakat soll in A5, A4, A3 und A2 nutzbar sein und der Text soll austauschbar sein.
Das Plakat soll gut zum Wochenmarkt passen und ehrliches, qualitativ hochwertiges Handwerk ausdrücken und vor allem Lust auf Maultaschen und Knödel machen. Es soll zu meinen Marktstand (Monza Rot) und dem Logo passen. Das Logo soll sehr präsent sein.

```html
<!DOCTYPE html>
<html lang="de">
<head>
<meta charset="utf-8">
<title>Rinnfalten &amp; Co – Plakat</title>
<link rel="stylesheet" href="https://fonts.googleapis.com/css2?family=Amaranth:wght@400;700&display=swap">
<style>
  :root {
    --monza-deep: #5a161a;
    --monza: #a61f26;
    --monza-dark: #86141a;
    --leaf: #8dc63f;
    --leaf-text: #9ccb3d;
    --mustard: #f2c21b;
    --badge: #ecc21f;
    --white: #ffffff;
    --plate: #0b0b0b;
  }
  html, body { margin: 0; padding: 0; overflow: hidden; background: var(--monza-deep); }
  .poster {
    position: relative;
    width: 714px;
    height: 1200px;
    overflow: hidden;
    background: var(--monza-deep);
    font-family: "Amaranth", sans-serif;
    color: var(--white);
  }
  .poster-art { position: absolute; inset: 0; width: 714px; height: 1200px; display: block; }
  .brand {
    position: absolute;
    left: 312px; top: 96px;
    font-size: 38px; font-weight: 400;
    color: var(--white);
    white-space: nowrap;
    line-height: 1;
  }
  .headline {
    position: absolute;
    left: 0; width: 714px; top: 620px;
    margin: 0;
    text-align: center;
    font-weight: 700;
    font-size: 62px;
    line-height: 76px;
    letter-spacing: -0.5px;
  }
  .headline .accent { color: var(--leaf-text); }
  .tagline {
    position: absolute;
    left: 0; width: 714px; top: 790px;
    margin: 0;
    text-align: center;
    font-size: 19px;
  }
  .today-label {
    position: absolute;
    left: 168px; top: 900px;
    font-size: 14px; line-height: 14px;
    text-align: right; width: 62px;
  }
  .product-list {
    position: absolute;
    left: 266px; top: 845px;
    margin: 0; padding: 0; list-style: none;
    color: var(--mustard);
    font-size: 23px; line-height: 34px;
  }
  .market-note {
    position: absolute;
    left: 242px; width: 232px; top: 1024px;
    text-align: center;
    font-size: 19px;
    color: var(--monza);
  }
  .market-note strong { font-weight: 700; }
  .love-badge {
    position: absolute;
    left: 546px; top: 548px; width: 144px;
    text-align: center;
    color: var(--monza);
    font-weight: 700;
    font-size: 23px; line-height: 23px;
  }
</style>
</head>
<body>
<div class="poster">
  <svg class="poster-art" viewBox="0 0 786 1192" preserveAspectRatio="none" aria-hidden="false">
    <defs>
      <linearGradient id="stageFill" x1="0" y1="0" x2="0" y2="1">
        <stop offset="0" stop-color="#b3232b"/>
        <stop offset="1" stop-color="#87141a"/>
      </linearGradient>
      <radialGradient id="stageGlow" cx="0.5" cy="0.3" r="0.6">
        <stop offset="0" stop-color="#c02a31" stop-opacity="0.6"/>
        <stop offset="1" stop-color="#c02a31" stop-opacity="0"/>
      </radialGradient>
      <radialGradient id="dishTones" cx="0.45" cy="0.75" r="0.55">
        <stop offset="0" stop-color="#7d7a3a"/>
        <stop offset="0.35" stop-color="#4e4a22"/>
        <stop offset="0.7" stop-color="#141410"/>
        <stop offset="1" stop-color="#060606"/>
      </radialGradient>
    </defs>

    <!-- stage blob with green outline -->
    <path class="stage" fill="url(#stageFill)" stroke="var(--leaf)" stroke-width="4"
      d="M352 62 C370 30 420 40 470 55 C560 80 680 45 752 30 C770 25 764 60 760 120
         C748 300 742 600 752 820 C758 960 770 1060 752 1085 C735 1100 690 1090 620 1086
         C500 1078 380 1080 250 1088 C150 1094 60 1100 30 1080 C10 1060 30 1000 45 930
         C60 850 25 740 25 560 C25 420 10 300 18 230 C22 200 60 195 120 192
         C190 190 220 170 240 160 C300 190 360 175 380 130 C392 100 372 80 352 62 Z"/>
    <path d="M352 62 C370 30 420 40 470 55 C560 80 680 45 752 30 C770 25 764 60 760 120
         C748 300 742 600 752 820 C758 960 770 1060 752 1085 C735 1100 690 1090 620 1086
         C500 1078 380 1080 250 1088 C150 1094 60 1100 30 1080 C10 1060 30 1000 45 930
         C60 850 25 740 25 560 C25 420 10 300 18 230 C22 200 60 195 120 192
         C190 190 220 170 240 160 C300 190 360 175 380 130 C392 100 372 80 352 62 Z"
      fill="url(#stageGlow)"/>

    <!-- brand mark circle -->
    <circle class="brand-dot" cx="300" cy="130" r="34" fill="var(--mustard)"/>

    <!-- dish photo area -->
    <g role="img" aria-label="Foto: angebratene Maultaschen mit Salat, Tomaten und roten Zwiebeln auf schwarzem Teller">
      <path fill="url(#dishTones)"
        d="M66 596 C66 400 210 228 392 228 C560 228 690 370 700 545
           C600 580 500 592 400 586 C280 580 160 596 66 596 Z"/>
    </g>
    <!-- yellow wave under the dish -->
    <path d="M50 622 C180 580 320 590 440 592 C560 594 640 570 700 545"
      fill="none" stroke="var(--mustard)" stroke-width="3"/>

    <!-- love badge -->
    <path d="M556 520 C560 470 620 440 670 450 C710 460 728 500 722 540"
      fill="none" stroke="var(--mustard)" stroke-width="2.5"/>
    <circle cx="660" cy="540" r="80" fill="var(--badge)"/>
    <path d="M660 522 C640 508 634 490 646 484 C654 480 660 486 660 492 C660 486 666 480 674 484 C686 490 680 508 660 522 Z"
      fill="var(--monza)"/>

    <!-- market stall icon -->
    <g class="stall-icon" fill="none" stroke="var(--mustard)" stroke-width="3" stroke-linejoin="round">
      <path d="M178 858 L242 858 L254 880 L166 880 Z"/>
      <path d="M166 880 C166 892 184 892 184 880 C184 892 202 892 202 880 C202 892 220 892 220 880 C220 892 238 892 238 880 C238 892 254 892 254 880"/>
      <path d="M196 858 L192 880 M224 858 L228 880"/>
      <path d="M172 890 L172 930"/>
      <path d="M248 890 L248 898"/>
    </g>

    <!-- green speech bubble -->
    <path fill="var(--leaf)"
      d="M272 986 C290 976 360 982 420 988 C470 992 526 976 522 1010 C520 1030 520 1036 540 1040
         C460 1046 360 1044 300 1050 L290 1050 C280 1062 250 1072 236 1074
         C250 1062 262 1052 266 1040 C258 1020 258 994 272 986 Z"/>
  </svg>

  <div class="brand">Rinnfalten &amp; Co</div>

  <div class="love-badge">Mit Liebe<br>gemacht</div>

  <h1 class="headline">
    Echte <span class="accent">Maultaschen</span>.<br>
    Frische <span class="accent">Knödel</span>.
  </h1>

  <p class="tagline">Traditionelle Klassiker – frisch und handgemacht.</p>

  <div class="today-label">Heute<br>am Stand</div>
  <ul class="product-list">
    <li>Schwäbische Maultaschen</li>
    <li>Spinat-Ricotta Maultaschen</li>
    <li>Kartoffelknödel</li>
  </ul>

  <div class="market-note">Direkt vom <strong>Marktstand</strong></div>
</div>
</body>
</html>
```